Bref créative
Business Cards and Stationery for The Cheerful Parcel
The Cheerful Parcel
Traditional
Nora Whitcomb
Chief Executive Officer
24817 Halvern
Dunmore, MI 4735-1186
nora@thecheerfulparcel.example
www.thecheerfulparcel.example
This is my logo in AI

```html
<!DOCTYPE html>
<html lang="en">
<head>
<meta charset="utf-8">
<title>The Cheerful Parcel — Stationery</title>
<link rel="stylesheet" href="https://fonts.googleapis.com/css2?family=Questrial&display=swap">
<style>
  :root{
    --plum:#6d1d60;
    --blush:#f3a9a4;
    --paper:#ffffff;
    --stage:#f1f1f2;
    --ink-soft:#8a6a84;
  }
  *{margin:0;padding:0;box-sizing:border-box}
  html,body{width:1200px;height:936px;overflow:hidden}
  body{background:linear-gradient(#f7f7f8,var(--stage));font-family:"Questrial",sans-serif;position:relative}
  .sheet{position:absolute;background:var(--paper);box-shadow:0 2px 6px rgba(0,0,0,.18);overflow:hidden}
  .sheet svg.band{position:absolute;left:0;bottom:0;width:100%;display:block}
  .brand{color:var(--plum);font-family:"Questrial",sans-serif;font-weight:400;line-height:1;text-align:center}
  .tagline{color:var(--plum);font-weight:400;letter-spacing:.02em;text-align:center;white-space:nowrap}

  .letterhead{left:183px;top:36px;width:388px;height:575px}
  .letterhead .brand-block{position:absolute;left:18px;top:38px;width:110px}
  .letterhead .brand{font-size:16px}
  .letterhead .tagline{font-size:6px;margin-top:5px}
  .letterhead .contact{position:absolute;left:300px;top:36px;font-size:5px;line-height:8px;color:var(--ink-soft);font-style:normal}
  .letterhead .contact span{display:block;padding-left:8px;position:relative}
  .letterhead .contact span::before{content:"";position:absolute;left:0;top:2px;width:4px;height:4px;background:var(--plum)}

  .folder{left:634px;top:36px;width:459px;height:581px}
  .folder .brand-block{position:absolute;left:0;right:0;top:215px}
  .folder .brand{font-size:46px}
  .folder .tagline{font-size:18px;margin-top:16px;letter-spacing:.06em}

  .card{width:180px;left:43px}
  .card-front{top:657px;height:104px}
  .card-front .brand{font-size:10px;margin-top:10px}
  .card-front .tagline{font-size:4px;margin-top:3px}
  .card-front .person{position:absolute;left:10px;top:50px;color:var(--plum)}
  .card-front .person b{display:block;font-weight:400;font-size:7px}
  .card-front .person i{display:block;font-style:normal;font-size:4.5px;color:var(--ink-soft);margin-top:2px}
  .card-front .contact{position:absolute;left:95px;top:47px;font-size:4px;line-height:6.5px;color:var(--ink-soft)}
  .card-back{top:779px;height:101px}
  .card-back .brand{font-size:12px;margin-top:24px}
  .card-back .web{position:absolute;left:0;right:0;bottom:7px;text-align:center;color:#fff;font-size:5px;letter-spacing:.08em}

  .envelope{top:672px;width:434px;height:208px}
  .envelope-front{left:264px}
  .envelope-front .brand-block{position:absolute;left:12px;top:14px;width:86px}
  .envelope-front .brand{font-size:13px}
  .envelope-front .tagline{font-size:4.5px;margin-top:4px}
  .envelope-front .return{position:absolute;left:14px;top:64px;font-size:4.5px;line-height:7px;color:var(--ink-soft)}
  .envelope-back{left:736px}
  .envelope-back svg{position:absolute;left:0;top:0;width:100%;height:100%}
  .envelope-back .web{position:absolute;left:0;right:0;top:21px;text-align:center;color:#fff;font-size:9px;letter-spacing:.24em}
</style>
</head>
<body>

<section class="sheet letterhead" aria-label="Letterhead">
  <div class="brand-block">
    <div class="brand">The Cheerful<br>Parcel</div>
    <div class="tagline">Gifts to brighten her day</div>
  </div>
  <address class="contact">
    <span>24817 Halvern</span>
    <span>Dunmore, MI 4735-1186</span>
    <span>Tel 313-555-0142</span>
    <span>nora@thecheerfulparcel.example</span>
    <span>www.thecheerfulparcel.example</span>
  </address>
  <svg class="band" viewBox="0 0 388 60" preserveAspectRatio="none" height="60">
    <path d="M0 14 Q194 -2 388 8 L388 60 L0 60Z" fill="var(--blush)"/>
    <path d="M0 22 Q194 6 388 16 L388 60 L0 60Z" fill="var(--plum)"/>
  </svg>
</section>

<section class="sheet folder" aria-label="Presentation folder">
  <div class="brand-block">
    <div class="brand">The Cheerful<br>Parcel</div>
    <div class="tagline">Gifts to brighten her day</div>
  </div>
  <svg class="band" viewBox="0 0 459 64" preserveAspectRatio="none" height="64">
    <path d="M0 18 Q230 -2 459 8 L459 64 L0 64Z" fill="var(--blush)"/>
    <path d="M0 26 Q230 6 459 16 L459 64 L0 64Z" fill="var(--plum)"/>
  </svg>
</section>

<section class="sheet card card-front" aria-label="Business card front">
  <div class="brand">The Cheerful Parcel</div>
  <div class="tagline">Gifts to brighten her day</div>
  <div class="person"><b>Nora Whitcomb</b><i>Chief Executive Officer</i></div>
  <div class="contact">24817 Halvern<br>Dunmore, MI 4735-1186<br>Tel 313-555-0142<br>nora@thecheerfulparcel.example<br>www.thecheerfulparcel.example</div>
  <svg class="band" viewBox="0 0 180 20" preserveAspectRatio="none" height="20">
    <path d="M0 6 Q90 0 180 3 L180 20 L0 20Z" fill="var(--blush)"/>
    <path d="M0 9 Q90 3 180 6 L180 20 L0 20Z" fill="var(--plum)"/>
  </svg>
</section>

<section class="sheet card card-back" aria-label="Business card back">
  <div class="brand">The Cheerful Parcel</div>
  <svg class="band" viewBox="0 0 180 26" preserveAspectRatio="none" height="26">
    <path d="M0 8 Q90 0 180 4 L180 26 L0 26Z" fill="var(--blush)"/>
    <path d="M0 11 Q90 3 180 7 L180 26 L0 26Z" fill="var(--plum)"/>
  </svg>
  <div class="web">www.thecheerfulparcel.example</div>
</section>

<section class="sheet envelope envelope-front" aria-label="Envelope front">
  <div class="brand-block">
    <div class="brand">The Cheerful<br>Parcel</div>
    <div class="tagline">Gifts to brighten her day</div>
  </div>
  <div class="return">24817 Halvern, Dunmore, MI 4735-1186</div>
</section>

<section class="sheet envelope envelope-back" aria-label="Envelope back">
  <svg viewBox="0 0 434 208" preserveAspectRatio="none">
    <path d="M0 0 H434 V52 Q300 58 217 100 Q134 58 0 52Z" fill="var(--blush)"/>
    <path d="M0 0 H434 V45 Q300 51 217 92 Q134 51 0 45Z" fill="var(--plum)"/>
  </svg>
  <div class="web">www.thecheerfulparcel.example</div>
</section>

</body>
</html>
```